Logo and Business card design!

Welbrook Estates

We are a Property development and real estate company (needs a logo design).

Welbrook estates is based in Sydney Australia and will be dealing with high net worth individuals with a corporate background. The demographic of clients will be relatively youthful and savvy. We do development finance, property development and some portion of property sales

I'd like the 'Welbrook' part of the name to be strength of the title, with 'property' playing a very minor part, perhaps in tiny font somewhere off to the bottom or side or something

Thank you!

Target Market(s)

25-55 years old

Industry/Entity Type

Real Estate Development

Contact Information for Business Card

Please arrange this information as you see fit

Leon Brightwater
Managing Director
0417 582 273
leon@welbrookestates-example.com.au
www.welbrookestates-example.com.au

Logo Text

Welbrook estates

Font styles to use
Serif

Colors

Designer to choose colors to be used in the design.

Requirements
Must have
• PLEASE VIEW THE UPLOADED IMAGES AND EXAMPLES
• And please put 'property' in small letters at the bottom or to the side. I want it to play a minimalist role, with 'WELBROOK' being the feature
• Colours! Please make sure theyre mostly grey and white with possibly some other dark blue and maybe dark grey
Nice to have
• Please feel free to use whatever colors you like, the suggested colors are something I selected momentarily and dont necessarily reflect strict guidelines
Should not have
• NO pictures or shapes of houses. I dont want the logo design to be so literal in its imagery

```html
<!DOCTYPE html>
<html lang="en">
<head>
<meta charset="utf-8">
<title>Welbrook Estates – Business Card</title>
<link rel="stylesheet" href="https://fonts.googleapis.com/css2?family=Ubuntu:wght@400;500&display=swap">
<style>
  :root {
    --teal: #1a86a3;
    --cyan-band: #22a4cd;
    --cyan-light: #2ec4ea;
    --icon-bg: #5cc3e4;
    --grey-bar: #8a8a8a;
    --ink-dark: #3a3a3a;
    --ink-mid: #555555;
    --white: #ffffff;
    --edge: #d6d6d6;
  }
  * { box-sizing: border-box; margin: 0; padding: 0; }
  html, body {
    width: 876px; height: 1200px; overflow: hidden;
    background: var(--white);
    font-family: "Ubuntu", sans-serif;
  }
  .canvas { position: relative; width: 876px; height: 1200px; }

  .card { position: absolute; left: 20px; width: 820px; height: 481px; }

  /* Wordmark */
  .brand { position: absolute; display: flex; align-items: flex-start; gap: 20px; }
  .brand__square { width: 34px; height: 34px; flex: none; }
  .brand__text { display: flex; flex-direction: column; align-items: center; }
  .brand__name { font-weight: 400; letter-spacing: 1px; line-height: 1; }
  .brand__sub { font-weight: 400; text-transform: uppercase; line-height: 1; }

  /* Front */
  .card--front { top: 25px; background: var(--teal); }
  .card--front .brand { left: 189px; top: 215px; }
  .card--front .brand__square { margin-top: 16px; background: var(--cyan-light); }
  .card--front .brand__name { font-size: 76px; color: var(--cyan-light); }
  .card--front .brand__sub { font-size: 14px; letter-spacing: 7px; margin-top: 14px; color: var(--cyan-light); }

  /* Back */
  .card--back { top: 686px; background: var(--white); border: 1px solid var(--edge); }
  .back__topbar { position: absolute; left: -1px; right: -1px; top: -1px; height: 18px; background: var(--grey-bar); }
  .card--back .brand { left: 83px; top: 118px; gap: 14px; }
  .card--back .brand__square { width: 26px; height: 26px; margin-top: 10px; background: var(--cyan-band); }
  .card--back .brand__name { font-size: 46px; color: var(--ink-dark); }
  .card--back .brand__sub { font-size: 9px; letter-spacing: 5px; margin-top: 8px; color: var(--ink-dark); }

  .person { position: absolute; right: 73px; top: 114px; text-align: right; }
  .person__name { font-size: 34px; font-weight: 400; color: var(--teal); line-height: 1.1; }
  .person__title { font-size: 17px; color: var(--ink-mid); margin-top: 7px; margin-right: 2px; }

  .back__band { position: absolute; left: -1px; right: -1px; top: 277px; height: 27px; background: var(--cyan-band); }
  .back__footer { position: absolute; left: -1px; right: -1px; top: 304px; bottom: -1px; background: var(--teal); }

  .contacts { list-style: none; position: absolute; left: 54px; top: 42px; }
  .contacts__item { display: flex; align-items: center; height: 26px; margin-bottom: 15px; color: var(--white); font-size: 17px; }
  .contacts__icon { width: 28px; height: 28px; margin-right: 38px; flex: none; }
</style>
</head>
<body>
<main class="canvas">

  <section class="card card--front" aria-label="Card front">
    <div class="brand">
      <span class="brand__square"></span>
      <div class="brand__text">
        <span class="brand__name">WELBROOK</span>
        <span class="brand__sub">Estates</span>
      </div>
    </div>
  </section>

  <section class="card card--back" aria-label="Card back">
    <div class="back__topbar"></div>

    <div class="brand">
      <span class="brand__square"></span>
      <div class="brand__text">
        <span class="brand__name">WELBROOK</span>
        <span class="brand__sub">Estates</span>
      </div>
    </div>

    <div class="person">
      <h1 class="person__name">Leon Brightwater</h1>
      <p class="person__title">Managing Director</p>
    </div>

    <div class="back__band"></div>
    <div class="back__footer">
      <ul class="contacts">
        <li class="contacts__item">
          <svg class="contacts__icon" viewBox="0 0 28 28" aria-hidden="true">
            <circle cx="14" cy="14" r="14" fill="var(--icon-bg)"/>
            <rect x="10" y="7" width="8" height="14" rx="1.5" fill="none" stroke="#fff" stroke-width="1.8"/>
            <circle cx="14" cy="18" r="1" fill="#fff"/>
          </svg>
          <span>0417 582 273</span>
        </li>
        <li class="contacts__item">
          <svg class="contacts__icon" viewBox="0 0 28 28" aria-hidden="true">
            <circle cx="14" cy="14" r="14" fill="var(--icon-bg)"/>
            <circle cx="14" cy="14" r="7" fill="none" stroke="#fff" stroke-width="1.6"/>
            <ellipse cx="14" cy="14" rx="3" ry="7" fill="none" stroke="#fff" stroke-width="1.4"/>
            <line x1="7" y1="14" x2="21" y2="14" stroke="#fff" stroke-width="1.4"/>
          </svg>
          <span>www.welbrookestates-example.com.au</span>
        </li>
        <li class="contacts__item">
          <svg class="contacts__icon" viewBox="0 0 28 28" aria-hidden="true">
            <circle cx="14" cy="14" r="14" fill="var(--icon-bg)"/>
            <rect x="7.5" y="9" width="13" height="10" rx="1" fill="none" stroke="#fff" stroke-width="1.6"/>
            <polyline points="7.5,9.5 14,15 20.5,9.5" fill="none" stroke="#fff" stroke-width="1.6"/>
          </svg>
          <span>leon@welbrookestates-example.com.au</span>
        </li>
      </ul>
    </div>
  </section>

</main>
</body>
</html>
```